The Plaster & Resonance Craftworks Inc (PRCI)

Create a LOGO and Business Card design.

Colors: Black, Bright Yellow & Red

Description of company: commercial carpentry, metal framing, drywall, taping/spackling, demolition, rough/finish carpentry.

Target Market(s)

developers, architects, general contractors, construction managers

Industry/Entity Type

Business

```html
<!DOCTYPE html>
<html lang="en">
<head>
<meta charset="utf-8">
<title>Plaster &amp; Resonance Craftworks Inc — Business Card</title>
<link rel="stylesheet" href="https://fonts.googleapis.com/css2?family=Dosis:wght@500;700;800&display=swap">
<style>
  :root {
    --ink: #111111;
    --paper: #ffffff;
    --brand-red: #e3202a;
    --brand-yellow: #ffe600;
    --band-black: #050505;
  }
  * { box-sizing: border-box; margin: 0; padding: 0; }
  html, body {
    width: 1200px;
    height: 667px;
    overflow: hidden;
    background: var(--paper);
  }
  .card {
    position: relative;
    width: 1200px;
    height: 667px;
    background: var(--paper);
    font-family: "Dosis", sans-serif;
    color: var(--ink);
    text-transform: uppercase;
    overflow: hidden;
  }
  .card__graphics {
    position: absolute;
    inset: 0;
  }
  .holder-name {
    position: absolute;
    left: 72px;
    top: 118px;
    font-size: 38px;
    font-weight: 800;
    letter-spacing: 1px;
    color: var(--brand-red);
  }
  .contact-list {
    position: absolute;
    left: 70px;
    top: 200px;
    list-style: none;
  }
  .contact-list__item {
    display: flex;
    align-items: center;
    height: 64px;
    font-size: 27px;
    font-weight: 500;
    letter-spacing: 0.5px;
  }
  .contact-list__icon {
    width: 40px;
    height: 40px;
    margin-right: 126px;
    flex: none;
  }
  .brand {
    position: absolute;
    left: 800px;
    top: 318px;
    width: 360px;
    display: flex;
    align-items: center;
    gap: 16px;
  }
  .brand__mark {
    width: 34px;
    height: 34px;
    background: var(--brand-red);
    flex: none;
  }
  .brand__name {
    font-size: 30px;
    font-weight: 800;
    line-height: 1.05;
    color: var(--brand-red);
  }
  .services-band {
    position: absolute;
    left: 0;
    top: 480px;
    width: 1200px;
    height: 110px;
    background: var(--band-black);
    color: var(--paper);
    display: flex;
    align-items: center;
    justify-content: center;
    text-align: center;
    font-size: 25px;
    font-weight: 500;
    line-height: 1.45;
    letter-spacing: 0.5px;
    padding: 0 40px;
  }
</style>
</head>
<body>
<div class="card">
  <svg class="card__graphics" width="1200" height="667" viewBox="0 0 1200 667" aria-hidden="true">
    <g class="diagonal-stripes" stroke-width="7" stroke-linecap="butt">
      <line x1="590" y1="-5" x2="650" y2="40" stroke="var(--ink)"/>
      <line x1="640" y1="-5" x2="790" y2="105" stroke="var(--brand-yellow)"/>
      <line x1="675" y1="-5" x2="760" y2="58" stroke="var(--ink)"/>
      <line x1="720" y1="-5" x2="930" y2="150" stroke="var(--brand-red)"/>
      <line x1="760" y1="-5" x2="1040" y2="202" stroke="var(--ink)"/>
      <line x1="810" y1="-5" x2="1210" y2="290" stroke="var(--brand-yellow)"/>
      <line x1="850" y1="-5" x2="1210" y2="261" stroke="var(--brand-red)"/>
      <line x1="900" y1="-5" x2="1210" y2="224" stroke="var(--ink)"/>
      <line x1="950" y1="-5" x2="1210" y2="187" stroke="var(--brand-yellow)"/>
      <line x1="990" y1="-5" x2="1210" y2="157" stroke="var(--ink)"/>
      <line x1="1040" y1="-5" x2="1210" y2="120" stroke="var(--brand-red)"/>
      <line x1="1085" y1="-5" x2="1210" y2="87" stroke="var(--brand-yellow)"/>
      <line x1="1130" y1="-5" x2="1210" y2="54" stroke="var(--ink)"/>
    </g>
    <g class="edge-rules">
      <rect x="0" y="437" width="790" height="7" fill="var(--brand-red)"/>
      <rect x="0" y="449" width="790" height="7" fill="var(--brand-yellow)"/>
      <rect x="815" y="462" width="385" height="6" fill="var(--brand-yellow)"/>
      <rect x="815" y="470" width="385" height="6" fill="var(--brand-red)"/>
      <rect x="0" y="597" width="1200" height="7" fill="var(--brand-red)"/>
      <rect x="0" y="610" width="1200" height="7" fill="var(--brand-yellow)"/>
    </g>
  </svg>

  <div class="holder-name">Dan Mercer</div>

  <ul class="contact-list">
    <li class="contact-list__item">
      <svg class="contact-list__icon" viewBox="0 0 40 40" aria-label="Phone">
        <rect x="13" y="6" width="14" height="30" rx="3" fill="none" stroke="var(--ink)" stroke-width="3"/>
        <rect x="16" y="10" width="8" height="9" fill="var(--ink)"/>
        <line x1="15" y1="2" x2="15" y2="7" stroke="var(--ink)" stroke-width="3"/>
      </svg>
      <span>000 000 0000</span>
    </li>
    <li class="contact-list__item">
      <svg class="contact-list__icon" viewBox="0 0 40 40" aria-label="Email">
        <text x="20" y="30" text-anchor="middle" font-family="Dosis, sans-serif" font-size="32" font-weight="700" fill="var(--ink)">@</text>
      </svg>
      <span>mercer@plasterresonance.com</span>
    </li>
    <li class="contact-list__item">
      <svg class="contact-list__icon" viewBox="0 0 40 40" aria-label="Website">
        <path d="M4 14 H24 L34 20 L24 26 H4 Z" fill="none" stroke="var(--ink)" stroke-width="3" stroke-linejoin="round"/>
        <line x1="10" y1="20" x2="28" y2="20" stroke="var(--ink)" stroke-width="2"/>
      </svg>
      <span>www.plasterresonance.com</span>
    </li>
  </ul>

  <div class="brand">
    <span class="brand__mark"></span>
    <span class="brand__name">The Plaster &amp; Resonance Craftworks Inc</span>
  </div>

  <div class="services-band">
    For all your commercial carpentry, metal framing, drywall, taping/<br>
    spackling, demolition and rough/finish carpentry needs.
  </div>
</div>
</body>
</html>
```